Book cover entitled #GLOWBEYONDIT

Design front book cover (self-self-portait photos included) for my first book entitled -

#GLOWBEYONDIT (may be best to have different shades of colour for glow beyond it to stand off you). I'm intentionally choosing a title that is essentially a hashtag.

Subtitle - Rewriting quiet inner battles

Concept of cover - left side of my face is shaded with shame and right side is brighter and hopeful. I have also include my logo.

Link for photos
https://www.filqorvex.com/sh/tq7mxd2kw9pl41a/BBR8NpXwQ3hLm6TzvKe2YUJ5b?dl=0

Target Market(s)

People (or friends & family) suffering with the shame of mental health struggles

Industry/Entity Type

Mental Health

Font styles to use
Other font styles liked:
• Avenir

Colors
3276b5
85acd3
cfdeed

Requirements
Must have
• Relatable, contemporary, authentic & compelling
• Link for photos
• https://www.filqorvex.com/sh/tq7mxd2kw9pl41a/BBR8NpXwQ3hLm6TzvKe2YUJ5b?dl=0
Nice to have
• Abstract & creative
Should not have
• Cheesy, plastic, pedestrian etc

```html
<!DOCTYPE html>
<html lang="en">
<head>
<meta charset="utf-8">
<title>#GLOWBEYONDIT — Book Cover</title>
<link href="https://fonts.googleapis.com/css2?family=Nunito+Sans:wght@300;400;600&display=swap" rel="stylesheet">
<style>
  :root {
    --stage: #eeeeee;
    --ink-deep: #0a0e1a;
    --frame-line: rgba(207, 222, 237, 0.6);
    --brand-blue: #3276b5;
    --brand-mid: #85acd3;
    --brand-pale: #cfdeed;
    --title-dim: #4a5364;
    --title-bright: #f4f6fa;
    --sub-rose: #e2708a;
    --sub-peach: #f2b07a;
    --logo-ink: #8ea3bd;
  }
  * { margin: 0; padding: 0; box-sizing: border-box; }
  html, body {
    width: 1200px; height: 1000px; overflow: hidden;
    background: var(--stage);
    font-family: "Nunito Sans", "Avenir Next", Avenir, sans-serif;
  }
  .canvas { position: relative; width: 1200px; height: 1000px; }
  .cover {
    position: absolute; left: 313px; top: 25px;
    width: 574px; height: 858px; overflow: hidden;
    background: var(--ink-deep);
  }
  .cover-art { position: absolute; inset: 0; width: 100%; height: 100%; }
  .author-mark {
    position: absolute; left: 34px; top: 28px;
    display: flex; flex-direction: column; align-items: flex-start; gap: 6px;
  }
  .author-mark__square { width: 44px; height: 44px; background: var(--brand-blue); }
  .author-mark__name {
    font-size: 15px; font-weight: 400; color: var(--logo-ink); letter-spacing: 0.5px;
  }
  .title {
    position: absolute; left: 0; right: 0; top: 496px;
    text-align: center; font-weight: 400; font-size: 60px; letter-spacing: 0.5px;
    line-height: 1; white-space: nowrap;
  }
  .title__shade { color: var(--title-dim); }
  .title__glow { color: var(--title-bright); text-shadow: 0 0 18px rgba(133,172,211,0.45); }
  .subtitle {
    position: absolute; right: 22px; top: 664px;
    text-align: right; font-weight: 300; font-size: 40px; line-height: 51px;
    text-transform: uppercase; letter-spacing: 0.3px; white-space: nowrap;
    background: linear-gradient(180deg, var(--sub-rose), var(--sub-peach));
    -webkit-background-clip: text; background-clip: text; color: transparent;
  }
</style>
</head>
<body>
<div class="canvas">
  <section class="cover">
    <svg class="cover-art" viewBox="0 0 574 858">
      <defs>
        <linearGradient id="backdrop" x1="0" x2="1">
          <stop offset="0" stop-color="#070a14"/>
          <stop offset="0.5" stop-color="#0c1220"/>
          <stop offset="1" stop-color="#161c30"/>
        </linearGradient>
        <radialGradient id="emberGlow" cx="0.82" cy="0.14" r="0.42">
          <stop offset="0" stop-color="#a8303a" stop-opacity="0.6"/>
          <stop offset="1" stop-color="#a8303a" stop-opacity="0"/>
        </radialGradient>
        <radialGradient id="cornerFlare" cx="0.98" cy="0.01" r="0.22">
          <stop offset="0" stop-color="#ffffff" stop-opacity="0.95"/>
          <stop offset="0.3" stop-color="#85acd3" stop-opacity="0.55"/>
          <stop offset="1" stop-color="#3276b5" stop-opacity="0"/>
        </radialGradient>
        <linearGradient id="portraitSplit" x1="0" x2="1">
          <stop offset="0" stop-color="#10151f"/>
          <stop offset="0.49" stop-color="#1b2232"/>
          <stop offset="0.51" stop-color="#4a4f5c"/>
          <stop offset="1" stop-color="#262d42"/>
        </linearGradient>
        <linearGradient id="portraitFade" x1="0" y1="0" x2="0" y2="1">
          <stop offset="0" stop-color="#fff" stop-opacity="0"/>
          <stop offset="0.12" stop-color="#fff" stop-opacity="1"/>
          <stop offset="1" stop-color="#fff" stop-opacity="1"/>
        </linearGradient>
        <mask id="portraitMask">
          <rect x="0" y="0" width="574" height="858" fill="url(#portraitFade)"/>
        </mask>
        <linearGradient id="centerBeam" x1="0" x2="1">
          <stop offset="0" stop-color="#3276b5" stop-opacity="0"/>
          <stop offset="0.5" stop-color="#e8f1ff" stop-opacity="0.9"/>
          <stop offset="1" stop-color="#3276b5" stop-opacity="0"/>
        </linearGradient>
      </defs>
      <rect width="574" height="858" fill="url(#backdrop)"/>
      <rect width="574" height="858" fill="url(#emberGlow)"/>
      <rect width="574" height="858" fill="url(#cornerFlare)"/>
      <g role="img" aria-label="Self-portrait of the author seated in a navy jacket, left half of the face in shadow and right half lit, hands clasped, night city lights behind">
        <rect class="portrait-area" x="40" y="120" width="520" height="738" rx="40"
              fill="url(#portraitSplit)" opacity="0.85" mask="url(#portraitMask)"/>
      </g>
      <rect class="center-beam" x="276" y="360" width="22" height="260" fill="url(#centerBeam)" opacity="0.7"/>
      <g class="diamond-frames" fill="none" stroke="var(--frame-line)" stroke-width="1.6">
        <polyline points="232,0 7,425 214,858"/>
        <polyline points="347,0 567,425 375,858"/>
        <line x1="287" y1="0" x2="287" y2="858"/>
      </g>
    </svg>

    <div class="author-mark">
      <span class="author-mark__square"></span>
      <span class="author-mark__name">ned calloway</span>
    </div>

    <h1 class="title"><span class="title__shade">#GLOW</span><span class="title__glow">BEYONDIT</span></h1>

    <p class="subtitle">Rewriting<br>quiet inner<br>battles</p>
  </section>
</div>
</body>
</html>
```